QDL Kids Choir

Card to hand out or mail out with our own mailing labels. Needs to be appealing to families with children ages 4 yrs through 6th grade, who have an interest in musical experiences for the kids in a contemporary Bible teaching/church setting. We have 3 different kids choirs: 4-yr-old & Kindergarten Choir, 1st-3rd grade choir, and 4th-6th grade choir. This is a FREE after-school program every Tuesday from 3:30-5:00. Transportation for grades 1-6 from local schools is provided. Parents should expect their children to experience fun, friends, music, recreation, games, snacks, character building, Bible teaching, in an encouraging church environment.

Church

• Bight colors

```html
<!DOCTYPE html>
<html lang="en">
<head>
<meta charset="utf-8">
<title>QDL Kids Choir – After-School Postcard</title>
<link href="https://fonts.googleapis.com/css2?family=Arimo:wght@700&family=Roboto+Condensed:wght@400&display=swap" rel="stylesheet">
<style>
  :root {
    --yellow-top: #f7c61c;
    --yellow-bottom: #efa01e;
    --blue: #1b8ccd;
    --blue-dark: #0f5f98;
    --blue-light: #36aee3;
    --band-blue: #128ad0;
    --ink-blue: #1f6db3;
    --white: #ffffff;
    --tick-green: #6cae2e;
    --tick-bg: #fff3b8;
    --rule: #dcdcdc;
    --stamp-border: #cfcfcf;
  }
  * { margin: 0; padding: 0; box-sizing: border-box; }
  html, body { width: 1200px; height: 930px; overflow: hidden; background: var(--white); }
  .postcard { position: relative; width: 1200px; height: 930px; background: var(--white); }

  /* Front panel */
  .promo-panel {
    position: absolute; left: 0; top: 0; width: 562px; height: 760px;
    background: linear-gradient(180deg, var(--yellow-top) 0%, var(--yellow-bottom) 100%);
    border-right: 2px solid #e9e4d2;
    overflow: hidden;
    font-family: "Arimo", Arial, sans-serif;
    font-weight: 700;
    color: var(--white);
  }
  .panel-shapes { position: absolute; inset: 0; width: 100%; height: 100%; }
  .headline {
    position: absolute; left: 84px; top: 210px;
    text-shadow: 1px 2px 3px rgba(0,0,0,.35);
  }
  .headline span { display: block; font-size: 30px; line-height: 32px; letter-spacing: .2px; }
  .photo-area {
    position: absolute; left: 78px; top: 285px; width: 440px; height: 168px;
    background: linear-gradient(135deg, #8fbf5a 0%, #d8b48a 45%, #6f9f3f 100%);
    border: 2px solid rgba(255,255,255,.7);
    box-shadow: 0 2px 6px rgba(0,0,0,.3);
  }
  .benefit-list { list-style: none; position: absolute; font-size: 29px; line-height: 34px; text-shadow: 1px 2px 3px rgba(0,0,0,.35); }
  .benefit-list.col-one { left: 86px; top: 468px; }
  .benefit-list.col-two { left: 297px; top: 466px; }
  .benefit-list li { display: flex; align-items: center; gap: 10px; height: 34.5px; }
  .tick { width: 24px; height: 24px; flex: none; filter: drop-shadow(1px 1px 1px rgba(0,0,0,.25)); }
  .setting-line {
    position: absolute; left: 60px; top: 606px; width: 440px; text-align: center;
    font-size: 29px; line-height: 32px; text-shadow: 1px 2px 3px rgba(0,0,0,.35);
  }
  .transport-band {
    position: absolute; left: 0; top: 693px; width: 562px; height: 67px;
    background: var(--band-blue);
    padding: 5px 0 0 162px;
    font-size: 25px; line-height: 28px;
  }

  /* Mailing side */
  .contact-list {
    list-style: none; position: absolute; left: 596px; top: 74px;
    font-family: "Roboto Condensed", "Arial Narrow", sans-serif;
    color: var(--ink-blue); font-size: 24px; line-height: 24px;
  }
  .contact-list li { display: flex; align-items: flex-start; gap: 8px; margin-bottom: 22px; }
  .contact-list li.address { margin-bottom: 22px; }
  .contact-icon { width: 22px; height: 22px; flex: none; margin-top: 1px; fill: var(--ink-blue); }
  .stamp-box {
    position: absolute; left: 907px; top: 34px; width: 266px; height: 266px;
    border: 2px solid var(--stamp-border);
  }
  .address-rule {
    position: absolute; left: 632px; width: 495px; height: 3px; background: var(--rule);
  }
</style>
</head>
<body>
<svg width="0" height="0" style="position:absolute">
  <symbol id="tick-box" viewBox="0 0 24 24">
    <rect x="1.5" y="1.5" width="21" height="21" rx="5" fill="var(--tick-bg)" stroke="var(--tick-green)" stroke-width="2"/>
    <path d="M6 12.5l4 4 8-10" fill="none" stroke="var(--tick-green)" stroke-width="3" stroke-linecap="round" stroke-linejoin="round"/>
  </symbol>
</svg>

<main class="postcard">
  <section class="promo-panel">
    <svg class="panel-shapes" viewBox="0 0 375 507" preserveAspectRatio="none" aria-hidden="true">
      <polygon points="0,44 375,32 375,132 0,98" fill="var(--blue)"/>
      <polygon points="318,36 375,32 375,132 290,129" fill="var(--blue-dark)"/>
      <polygon points="0,150 48,292 0,310" fill="var(--blue-light)"/>
    </svg>

    <h1 class="headline">
      <span>FREE after-school program</span>
      <span>every Tuesday from 3:30-5:00.</span>
    </h1>

    <div class="photo-area" role="img" aria-label="Photo of children lying on the grass reading a book together"></div>

    <ul class="benefit-list col-one">
      <li><svg class="tick"><use href="#tick-box"/></svg>fun</li>
      <li><svg class="tick"><use href="#tick-box"/></svg>friends</li>
      <li><svg class="tick"><use href="#tick-box"/></svg>music</li>
      <li><svg class="tick"><use href="#tick-box"/></svg>recreation</li>
    </ul>
    <ul class="benefit-list col-two">
      <li><svg class="tick"><use href="#tick-box"/></svg>games</li>
      <li><svg class="tick"><use href="#tick-box"/></svg>snacks</li>
      <li><svg class="tick"><use href="#tick-box"/></svg>building</li>
      <li><svg class="tick"><use href="#tick-box"/></svg>Bible teaching</li>
    </ul>

    <p class="setting-line">in an encouraging church<br>environment.</p>

    <p class="transport-band">Transportation for grades 1-6<br>from local schools is provided.</p>
  </section>

  <ul class="contact-list">
    <li class="address">
      <svg class="contact-icon" viewBox="0 0 24 24" aria-hidden="true"><path d="M12 2L1 12h3v10h6v-6h4v6h6V12h3z"/></svg>
      <span>2450 W. Maple Grove<br>Cedar Falls, Oklahoma 73099</span>
    </li>
    <li>
      <svg class="contact-icon" viewBox="0 0 24 24" aria-hidden="true"><path d="M6.6 10.8a15 15 0 006.6 6.6l2.2-2.2a1 1 0 011-.25 11.4 11.4 0 003.6.57 1 1 0 011 1V20a1 1 0 01-1 1A17 17 0 013 4a1 1 0 011-1h3.5a1 1 0 011 1c0 1.25.2 2.45.57 3.6a1 1 0 01-.25 1z"/></svg>
      <span>580-555-0148</span>
    </li>
    <li>
      <svg class="contact-icon" viewBox="0 0 24 24" aria-hidden="true"><g fill="none" stroke="var(--ink-blue)" stroke-width="1.8"><circle cx="12" cy="12" r="10"/><ellipse cx="12" cy="12" rx="4.5" ry="10"/><path d="M2 12h20M4 6.5h16M4 17.5h16"/></g></svg>
      <span>www.qdlkidschoir.com</span>
    </li>
  </ul>

  <div class="stamp-box" aria-label="Stamp area"></div>

  <div class="address-rule" style="top:420px"></div>
  <div class="address-rule" style="top:504px"></div>
  <div class="address-rule" style="top:587px"></div>
  <div class="address-rule" style="top:668px"></div>
</main>
</body>
</html>
```